Halvorsen Partners Business Card

Halvorsen Partners Civil Construction
Dorian Halvorsen
CEO
555-318-4076
Dorian@HalvorsenCivil.example
www.HalvorsenCivil.example
Site Development
Utility Construction
Excavation
48730 County Route 19
Land O' Lakes, FL 34999

Target Market(s)

Construction and government

Industry/Entity Type

Business

Contact Information for Business Card

I want an unique design that make a statement

Number of Pages Required

1 page

Font styles to use
Other font styles liked:

Colors

Designer to choose colors to be used in the design.

Requirements
Must have
• unique design, feel free to modify or change the color of my logo.
Nice to have
• extra design features like spot UV, foil accents, color edges, unique paper, or any thing that would make my card pop.
• I like the feel of the image that I attached

```html
<!DOCTYPE html>
<html lang="en">
<head>
<meta charset="utf-8">
<title>Halvorsen Partners Business Card</title>
<link rel="stylesheet" href="https://fonts.googleapis.com/css2?family=Lato:wght@700&family=Open+Sans:wght@400;600&display=swap">
<style>
  :root {
    --page-bg: #d8d4cf;
    --card-face: #efedea;
    --card-face-shade: #dcdad8;
    --navy: #1c2359;
    --navy-deep: #121841;
    --navy-light: #2a3270;
    --rose-gold: #cfac9c;
    --silver: #e9e2dc;
    --strip-top: #4a4644;
    --strip-bottom: #2b2827;
  }
  * { box-sizing: border-box; margin: 0; padding: 0; }
  html, body { width: 1200px; height: 970px; overflow: hidden; }
  body {
    background: var(--page-bg);
    position: relative;
    font-family: "Open Sans", Arial, sans-serif;
  }
  .business-card {
    position: absolute;
    left: 100px; top: 200px;
    width: 1000px; height: 569px;
    background: linear-gradient(135deg, var(--card-face) 0%, #f7f6f4 45%, var(--card-face-shade) 100%);
    box-shadow: 0 18px 40px rgba(0,0,0,.25);
    overflow: hidden;
  }
  .brand {
    position: absolute;
    left: 198px; top: 96px;
    display: flex; align-items: center; gap: 30px;
  }
  .brand-square {
    width: 112px; height: 112px;
    background: var(--navy);
  }
  .brand-name {
    font-family: "Lato", Arial, sans-serif;
    font-weight: 700;
    color: var(--navy);
    text-transform: uppercase;
    line-height: 1;
  }
  .brand-name .line-main { display: block; font-size: 44px; letter-spacing: .01em; }
  .brand-name .line-sub { display: block; font-size: 26px; letter-spacing: .26em; margin-top: 16px; }

  .contact-band {
    position: absolute;
    left: 0; top: 304px;
    width: 100%; height: 200px;
    background: linear-gradient(180deg, var(--navy-light) 0%, var(--navy) 45%, var(--navy-deep) 100%);
  }
  .person {
    position: absolute;
    right: 542px; top: 60px;
    text-align: right;
    color: var(--silver);
  }
  .person-name { font-size: 34px; font-weight: 600; letter-spacing: .01em; text-transform: uppercase; line-height: 1.1; }
  .person-title { font-size: 27px; font-weight: 400; color: var(--rose-gold); margin-top: 6px; }
  .band-divider {
    position: absolute;
    left: 499px; top: 48px;
    width: 2px; height: 98px;
    background: var(--rose-gold);
  }
  .contact-list {
    position: absolute;
    left: 540px; top: 44px;
    list-style: none;
    color: var(--rose-gold);
    font-size: 25px;
  }
  .contact-list li { display: flex; align-items: center; gap: 14px; height: 36px; }
  .contact-icon { width: 28px; height: 28px; flex: none; }

  .services-strip {
    position: absolute;
    left: 0; top: 504px;
    width: 100%; height: 65px;
    background: linear-gradient(180deg, var(--strip-top), var(--strip-bottom));
    border-top: 2px solid var(--silver);
    display: flex; align-items: center; justify-content: center;
    color: var(--silver);
    font-size: 25px;
  }
  .services-strip .sep { margin: 0 10px; color: var(--rose-gold); }
</style>
</head>
<body>
  <article class="business-card">
    <header class="brand">
      <div class="brand-square"></div>
      <h1 class="brand-name">
        <span class="line-main">Halvorsen Partners</span>
        <span class="line-sub">Civil Construction</span>
      </h1>
    </header>

    <section class="contact-band">
      <div class="person">
        <p class="person-name">Dorian Halvorsen</p>
        <p class="person-title">CEO</p>
      </div>
      <div class="band-divider"></div>
      <ul class="contact-list">
        <li>
          <svg class="contact-icon" viewBox="0 0 28 28" aria-hidden="true">
            <rect width="28" height="28" rx="3" fill="#cfac9c"/>
            <path d="M6 11c0-3 4-4 8-4s8 1 8 4v2h-4v-2h-8v2H6z" fill="#1c2359"/>
            <rect x="8" y="14" width="12" height="8" rx="1" fill="#1c2359"/>
          </svg>
          <span>555-318-4076</span>
        </li>
        <li>
          <svg class="contact-icon" viewBox="0 0 28 28" aria-hidden="true">
            <rect width="28" height="28" rx="3" fill="#cfac9c"/>
            <rect x="5" y="8" width="18" height="12" fill="none" stroke="#1c2359" stroke-width="1.8"/>
            <path d="M5 8l9 7 9-7M5 20l7-6M23 20l-7-6" fill="none" stroke="#1c2359" stroke-width="1.5"/>
          </svg>
          <span>Dorian@HalvorsenCivil.example</span>
        </li>
        <li>
          <svg class="contact-icon" viewBox="0 0 28 28" aria-hidden="true">
            <rect width="28" height="28" rx="3" fill="#cfac9c"/>
            <circle cx="14" cy="14" r="8" fill="none" stroke="#1c2359" stroke-width="1.6"/>
            <ellipse cx="14" cy="14" rx="3.5" ry="8" fill="none" stroke="#1c2359" stroke-width="1.3"/>
            <path d="M6 14h16M7.5 10h13M7.5 18h13" stroke="#1c2359" stroke-width="1.2"/>
          </svg>
          <span>www.HalvorsenCivil.example</span>
        </li>
      </ul>
    </section>

    <footer class="services-strip">
      <span>Site Development</span><span class="sep">|</span>
      <span>Utility Construction</span><span class="sep">|</span>
      <span>Excavation</span>
    </footer>
  </article>
</body>
</html>
```